Driver License Monitoring Application Marketing Website

We need a new web design for our web application. The product is called "PermitPulse." We provide a driver license monitoring service to companies and local government bodies with driver fleets. Our current website is available at www.permitpulse-example.com.

I prefer a clean, single-page design with good SEO. Attached are some PDFs with data about the project.

Target Market(s)

Companies with driver fleets, local government.

Industry/Entity Type

Government

Coding

Coded - Design and coding required

Number of Pages Required

1 page

Colors
000000

Requirements
Must have
• Content from current www.permitpulse-example.com and attached PDFs.
Nice to have
• Prefer a simple Bootstrap or similar design for easy editing.
• Room for a simple video explanation of how the product works (we don't have an actual video yet)

```html
<!DOCTYPE html>
<html lang="en">
<head>
<meta charset="utf-8">
<title>PermitPulse – Driver License Monitoring</title>
<link rel="stylesheet" href="https://fonts.googleapis.com/css2?family=Cinzel:wght@400;700&family=Open+Sans:wght@400;600;700;800&display=swap">
<style>
:root{
  --red:#c8151b;
  --red-dark:#a10e13;
  --ink:#1f1f1f;
  --bar:#262626;
  --dark:#2a2a2a;
  --grey-bg:#dcdcdc;
  --text-grey:#7a7a7a;
  --white:#ffffff;
  --footer:#2b2b2b;
}
*{margin:0;padding:0;box-sizing:border-box}
html,body{width:826px;height:1200px;overflow:hidden}
body{position:relative;font-family:"Open Sans",Arial,sans-serif;background:var(--white);color:var(--ink)}
.abs{position:absolute}

.top-bar{left:0;top:0;width:826px;height:38px;background:var(--bar);font-size:9px;color:#9a9a9a}
.top-bar .address{left:41px;top:13px}
.top-bar .contact{right:41px;top:13px}
.top-bar .contact b{color:#eee;font-weight:400;margin-right:10px}
.top-bar .contact .mail{color:var(--red)}

.site-header{left:0;top:38px;width:826px;height:66px;background:var(--white);border-bottom:1px solid #e4e4e4}
.brand{left:41px;top:20px;font-family:"Cinzel",serif;font-weight:700;font-size:24px;color:var(--ink);letter-spacing:.5px}
.main-nav a{position:absolute;top:0;height:66px;line-height:66px;font-size:12px;color:#333;text-decoration:none}
.main-nav .active{left:351px;width:43px;background:var(--red);color:var(--white);text-align:center}

.hero{left:0;top:104px;width:826px;height:318px;background:linear-gradient(100deg,#8a3a1c 0%,#e6b45c 30%,#f4d79a 45%,#c98a4a 65%,#e9c79a 85%,#a55a3a 100%)}
.hero-caption{left:41px;top:75px;width:256px;height:175px;background:rgba(90,80,65,.72);padding:20px 12px 0}
.hero-caption .kicker{font-family:"Cinzel",serif;font-size:14px;color:#eee}
.hero-caption h1{font-weight:800;font-size:29px;color:var(--white);letter-spacing:1px;line-height:1.2}
.hero-caption p{font-size:9px;color:#f3f3f3;line-height:15px;margin-top:8px}
.btn{display:inline-block;background:var(--red);border:1px solid var(--red-dark);color:var(--white);font-size:10px;font-weight:700;border-radius:3px;padding:6px 8px;box-shadow:inset 0 1px 0 rgba(255,255,255,.2)}
.hero-caption .btn{margin-top:12px}
.dot{position:absolute;top:293px;width:9px;height:9px;border-radius:50%;background:var(--white)}
.dot.on{background:var(--red)}

.industries{left:0;top:422px;width:826px;height:298px;background:var(--dark)}
.section-title{font-family:"Cinzel",serif;font-size:20px;font-weight:400}
.industries .section-title{left:41px;top:24px;color:var(--white)}
.card{position:absolute;top:76px;width:173px;height:188px;background:var(--white);box-shadow:0 6px 8px rgba(0,0,0,.4)}
.card .photo{width:173px;height:150px}
.card .label{height:38px;line-height:38px;padding-left:8px;font-size:11px;font-weight:600;color:var(--red);background:linear-gradient(#fff,#eaeaea)}

.features{left:0;top:720px;width:826px;height:392px;background:var(--grey-bg)}
.feature{position:absolute;top:30px;width:231px}
.feature .section-title{color:var(--ink);margin-left:2px}
.feature .photo{margin-top:16px;width:231px;height:108px;border:3px solid var(--white);box-shadow:0 1px 3px rgba(0,0,0,.25)}
.feature p{font-size:9px;color:var(--text-grey);line-height:15.5px;margin-top:18px}
.feature p + p{margin-top:15px}
.feature .btn{margin-top:22px;font-size:10.5px;padding:6px 8px}

.site-footer{left:0;top:1112px;width:826px;height:88px;background:var(--footer)}
.footer-links{left:41px;top:26px;font-size:11px;color:#999}
.footer-links span{margin:0 4px}
.copyright{left:41px;top:46px;font-size:9px;color:#8a8a8a}
.social{position:absolute;top:23px;width:30px;height:30px;border-radius:50%;border:2px solid #ddd}
</style>
</head>
<body>

<div class="top-bar abs">
  <div class="address abs">PermitPulse, Inc. 4100 Harbor View Rd., Ste 210, Lakeside, FL 33999</div>
  <div class="contact abs">Telephone: <b>1.555.010.2841</b> Fax: <b>1.555.010.2844</b> <span class="mail">Email: contact@permitpulse-example.com</span></div>
</div>

<header class="site-header abs">
  <div class="brand abs">PermitPulse</div>
  <nav class="main-nav">
    <a class="active" href="#">Home</a>
    <a href="#" style="left:424px">License Monitoring</a>
    <a href="#" style="left:562px">About Us</a>
    <a href="#" style="left:646px">Contact</a>
    <a href="#" style="left:723px">Client Login</a>
  </nav>
</header>

<section class="hero abs" role="img" aria-label="Sunlit view of a truck cab on the highway">
  <div class="hero-caption abs">
    <div class="kicker">DRIVER LICENSE</div>
    <h1>MONITORING</h1>
    <p>Track your fleet for safety and performance Monitor your drivers electronically.</p>
    <span class="btn">Read More</span>
  </div>
  <span class="dot" style="left:389px"></span>
  <span class="dot on" style="left:409px"></span>
  <span class="dot" style="left:430px"></span>
</section>

<section class="industries abs">
  <h2 class="section-title abs">OUR INDUSTRIES</h2>
  <div class="card" style="left:41px">
    <div class="photo" role="img" aria-label="White semi truck on the road" style="background:linear-gradient(160deg,#8fb0d0,#d8dde2 55%,#5a6470)"></div>
    <div class="label">COMMERCIAL SECTOR</div>
  </div>
  <div class="card" style="left:231px">
    <div class="photo" role="img" aria-label="Yellow school bus side lettering" style="background:linear-gradient(160deg,#f2c51e,#e0a800 60%,#4a4a3a)"></div>
    <div class="label">SCHOOL DISTRICTS</div>
  </div>
  <div class="card" style="left:421px">
    <div class="photo" role="img" aria-label="City skyline with office towers" style="background:linear-gradient(180deg,#b9c4cc,#8d8f8a 45%,#4f5558)"></div>
    <div class="label">GOVERNMENT</div>
  </div>
  <div class="card" style="left:612px">
    <div class="photo" role="img" aria-label="Red tanker truck" style="background:linear-gradient(160deg,#3a6fb0,#9fbfd8 45%,#c8352c 70%,#6b6b6b)"></div>
    <div class="label">INSURANCE INDUSTRY</div>
  </div>
</section>

<section class="features abs">
  <article class="feature" style="left:41px">
    <h2 class="section-title">ABOUT US</h2>
    <div class="photo" role="img" aria-label="White truck under a blue sky" style="background:linear-gradient(120deg,#3a78c0,#d9e4ee 50%,#8cc34a)"></div>
    <p>How many of your drivers currently have a suspended license? The answer may surprise you.</p>
    <p>Driving with a suspended license is the most commonly committed offense in America. In 2011, over 1.8 million licenses got suspended in Florida.</p>
    <span class="btn">Read More</span>
  </article>
  <article class="feature" style="left:298px">
    <h2 class="section-title">WHAT WE DO</h2>
    <div class="photo" role="img" aria-label="Highway through forest at sunset" style="background:linear-gradient(180deg,#c9a35a,#6e7a3a 45%,#5b5650)"></div>
    <p>How many of your drivers currently have a suspended license? The answer may surprise you.</p>
    <p>Driving with a suspended license is the most commonly committed offense in America. In 2011, over 1.8 million licenses got suspended in Florida.</p>
    <span class="btn">Read More</span>
  </article>
  <article class="feature" style="left:554px">
    <h2 class="section-title">OUR SECTORS</h2>
    <div class="photo" role="img" aria-label="Tanker truck on a multi-lane highway" style="background:linear-gradient(160deg,#6a9a3a,#8c9095 40%,#7a7e82 70%,#5f8f30)"></div>
    <p>How many of your drivers currently have a suspended license? The answer may surprise you.</p>
    <p>Driving with a suspended license is the most commonly committed offense in America. In 2011, over 1.8 million licenses got suspended in Florida.</p>
    <span class="btn">Read More</span>
  </article>
</section>

<footer class="site-footer abs">
  <div class="footer-links abs">Home<span>/</span>License Monitoring<span>/</span>About Us<span>/</span>Contact<span>/</span>Client Login</div>
  <div class="copyright abs">© 2015 permitpulse-example.com. All rights reserved.</div>
  <span class="social" style="left:666px;background:#2c4f8f" aria-label="Social link"></span>
  <span class="social" style="left:712px;background:#1e8fd1" aria-label="Social link"></span>
  <span class="social" style="left:756px;background:#e8661c" aria-label="Feed link"></span>
</footer>

</body>
</html>
```